Spiritual Healing bussiness needs logo/business card

Simple, clean looking logo/card
For spiritual business with healing services and occult rituals

Contact Information for Business Card

Needs my name: Tovin Harlowe
Business name: Velka Healing Shop
Services provided and worded in this way:

Reiki Healing
Tarot
Oils
Rituals Of Change

Can look occult like but with light energy.

Colors
0255a3
3276b5
85abd2
33a6d7
85cae6
0292cd

```html
<!DOCTYPE html>
<html lang="en">
<head>
<meta charset="utf-8">
<title>Velka Healing Shop — Business Card</title>
<link rel="stylesheet" href="https://fonts.googleapis.com/css2?family=Work+Sans:wght@400;500;700&family=Oswald:wght@500&display=swap">
<style>
  :root {
    --backdrop: #161616;
    --backdrop-edge: #0b0b0b;
    --card: #1e1e1e;
    --card-sheen: #2b2b2b;
    --ink-silver: #d9d9d9;
    --ink-soft: #a8a8a8;
    --ink-emboss: #121212;
    --emboss-light: rgba(255,255,255,0.08);
    --rule: #4a4a4a;
  }
  * { margin: 0; padding: 0; box-sizing: border-box; }
  html, body { width: 1200px; height: 900px; overflow: hidden; }
  body {
    background: radial-gradient(ellipse at 50% 40%, var(--backdrop) 0%, var(--backdrop-edge) 100%);
    font-family: "Work Sans", sans-serif;
    position: relative;
  }
  .card {
    position: absolute;
    left: 290px;
    width: 620px;
    height: 354px;
    background: linear-gradient(135deg, var(--card) 45%, var(--card-sheen) 80%, var(--card) 100%);
    box-shadow: 0 12px 30px rgba(0,0,0,0.6);
  }
  .card--front { top: 70px; }
  .card--back { top: 466px; }

  .brand-name {
    position: absolute;
    top: 130px; left: 0; right: 0;
    text-align: center;
    font-weight: 700;
    font-size: 40px;
    letter-spacing: 0.5px;
    color: var(--ink-silver);
  }
  .services {
    position: absolute;
    bottom: 34px; left: 0; right: 0;
    text-align: center;
    font-size: 14px;
    letter-spacing: 1px;
    color: var(--ink-soft);
  }

  .holder {
    position: absolute;
    top: 118px; left: 70px;
    width: 230px;
    text-align: right;
  }
  .holder-name {
    font-family: "Oswald", sans-serif;
    font-weight: 500;
    font-size: 40px;
    letter-spacing: 3px;
    text-transform: uppercase;
    color: var(--ink-emboss);
    text-shadow: 0 1px 0 var(--emboss-light), 0 -1px 0 rgba(0,0,0,0.6);
    line-height: 1.1;
  }
  .holder-role {
    font-size: 15px;
    letter-spacing: 1px;
    color: var(--ink-emboss);
    text-shadow: 0 1px 0 var(--emboss-light);
  }
  .divider {
    position: absolute;
    top: 118px; left: 325px;
    width: 1px; height: 70px;
    background: var(--rule);
  }
  .contact-list {
    position: absolute;
    top: 118px; left: 345px;
    list-style: none;
    font-size: 16px;
    letter-spacing: 0.5px;
    color: var(--ink-silver);
  }
  .contact-list li {
    display: flex;
    align-items: center;
    gap: 10px;
    height: 24px;
  }
  .contact-list svg { width: 11px; height: 11px; flex: none; }
  .address {
    position: absolute;
    bottom: 34px; left: 0; right: 0;
    text-align: center;
    font-size: 16px;
    letter-spacing: 1px;
    color: var(--ink-silver);
  }
</style>
</head>
<body>
  <section class="card card--front">
    <h1 class="brand-name">Velka Healing Shop</h1>
    <p class="services">Reiki Healing | Tarot | Oils | Rituals Of Change</p>
  </section>

  <section class="card card--back">
    <div class="holder">
      <p class="holder-name">Tovin Harlowe</p>
      <p class="holder-role">Director</p>
    </div>
    <div class="divider"></div>
    <ul class="contact-list">
      <li>
        <svg viewBox="0 0 12 12" aria-hidden="true"><path d="M2.5 1 L4.5 1 L5 3.5 L3.8 4.4 Q5 7 7.6 8.2 L8.5 7 L11 7.5 L11 9.5 Q10.5 11 9 11 Q1 10 1 3 Q1 1.5 2.5 1 Z" fill="var(--ink-soft)"/></svg>
        (555) 014-2290
      </li>
      <li>
        <svg viewBox="0 0 12 12" aria-hidden="true"><rect x="1" y="2.5" width="10" height="7" fill="none" stroke="var(--ink-soft)" stroke-width="1.2"/><path d="M1 2.5 L6 6.5 L11 2.5" fill="none" stroke="var(--ink-soft)" stroke-width="1.2"/></svg>
        info@velkahealingshop.com
      </li>
      <li>
        <svg viewBox="0 0 12 12" aria-hidden="true"><circle cx="6" cy="6" r="5" fill="none" stroke="var(--ink-soft)" stroke-width="1.1"/><ellipse cx="6" cy="6" rx="2.2" ry="5" fill="none" stroke="var(--ink-soft)" stroke-width="1"/><path d="M1 6 H11" stroke="var(--ink-soft)" stroke-width="1"/></svg>
        www.velkahealingshop.com
      </li>
    </ul>
    <p class="address">48b Marlow Lane, Eastbridge, NZ, 8042</p>
  </section>
</body>
</html>
```